Apartment Hotel
Zielgruppe
Apartment Hotel, verkauf von Hotelzimmer, bzw. Apartments. Für kurzreisende oder Langzeitaufenthalte, für Touristen , Geschäftsleuten, Firmen.
Wir stellen komplette 1 oder 2 Zimmerapartments mit Küche.
www.apartment-hotel-feldburg.de
Aufgabenstellung
modernes Logo , Briefpapier & Visitenkarten , Layout,
Platz für Name/Position: Hotelmanager

```html
<!DOCTYPE html>
<html lang="de">
<head>
<meta charset="utf-8">
<title>Feldburg Apartmenthotel – Visitenkarten</title>
<link href="https://fonts.googleapis.com/css2?family=Source+Sans+3:wght@400;600&display=swap" rel="stylesheet">
<style>
  :root {
    --backdrop: #6297ad;
    --card-white: #ffffff;
    --brand-green: #a3c86a;
    --name-green: #9cc464;
    --text-blue: #6a9bb3;
    --tint-green: #e6efd7;
    --tint-green-deep: #b4d282;
  }
  html, body {
    margin: 0;
    width: 1200px;
    height: 1200px;
    overflow: hidden;
    background: var(--backdrop);
    font-family: "Source Sans 3", "Helvetica Neue", Arial, sans-serif;
  }
  .stage { position: relative; width: 1200px; height: 1200px; }

  .card { position: absolute; width: 580px; height: 374px; overflow: hidden; }

  /* contact side */
  .card--contact { left: 508px; top: 304px; background: var(--card-white); }
  .card--contact .facade {
    position: absolute; left: 0; top: 96px; width: 290px; height: 278px;
    background: linear-gradient(180deg, rgba(230,239,215,0) 0%, var(--tint-green) 35%, var(--tint-green) 100%);
  }
  .contact { position: absolute; left: 306px; top: 110px; color: var(--text-blue); }
  .contact__name { margin: 0; font-size: 22px; font-weight: 600; color: var(--name-green); letter-spacing: 0.2px; line-height: 1; }
  .contact__role { margin: 9px 0 0; font-size: 13px; letter-spacing: 1px; text-transform: uppercase; line-height: 1; }
  .contact__address { margin: 18px 0 0; font-size: 15px; line-height: 24px; font-style: normal; }
  .contact__lines { margin: 10px 0 0; padding: 0; list-style: none; font-size: 15px; line-height: 24px; }
  .contact__lines b { font-weight: 600; display: inline-block; width: 16px; }
  .contact__web { margin: 10px 0 0; font-size: 15px; color: var(--name-green); line-height: 24px; }

  /* brand side */
  .card--brand { left: 118px; top: 559px; width: 583px; background: var(--brand-green); }
  .card--brand .facade {
    position: absolute; left: 0; top: 97px; width: 288px; height: 277px;
    background: linear-gradient(180deg, rgba(180,210,130,0) 0%, var(--tint-green-deep) 40%, var(--tint-green-deep) 100%);
  }
  .brand {
    position: absolute; left: 222px; top: 292px;
    display: flex; align-items: center; gap: 12px;
  }
  .brand__mark { width: 16px; height: 16px; background: var(--card-white); }
  .brand__name { font-size: 46px; font-weight: 400; letter-spacing: 3px; color: var(--card-white); line-height: 1; }
</style>
</head>
<body>
<main class="stage">

  <section class="card card--contact" aria-label="Visitenkarte Rückseite">
    <div class="facade" role="img" aria-label="Zarte Linienzeichnung der Hotelfassade als Hintergrunddekor"></div>
    <div class="contact">
      <h1 class="contact__name">Katrin Albers</h1>
      <p class="contact__role">Hotelmanager</p>
      <address class="contact__address">
        Apartment Hotel Feldburg<br>
        Gartenweg 14<br>
        99084 Erfurt
      </address>
      <ul class="contact__lines">
        <li><b>T</b>+493615550142</li>
        <li><b>F</b>+493615550199</li>
        <li><b>M</b>info@hotel-feldburg.de</li>
      </ul>
      <p class="contact__web">www.apartment-hotel-feldburg.de</p>
    </div>
  </section>

  <section class="card card--brand" aria-label="Visitenkarte Vorderseite">
    <div class="facade" role="img" aria-label="Helle Zeichnung der Hotelfassade als Hintergrunddekor"></div>
    <div class="brand">
      <span class="brand__mark"></span>
      <span class="brand__name">FELDBURG</span>
    </div>
  </section>

</main>
</body>
</html>
```